Letterhead Design Project

Consulting Company , we want a letterhead incorporating both the picture provided and the logo provided. The font name is monotype corsiva.
Target Market(s)
Dentist
Industry/Entity Type
Consulting
Font styles to use
Other font styles liked:
- monotype corsiva

Colors
0455a3
Requirements
Must have
- the logo, the picture (see attached), the website name, the email. and the phone numbers.
- Website: www.trquillarisadvisory.solutions
- Email: will be provided to the winner, please use placeholder
- Phone numbers:
- Petra Hallum 5829017763
- Owen Vrastik 6148250397

Nice to have
- a swoop or wave across the bottom. a line up the side. I don't know guys. design something unique and professional.

Should not have
- arrows pointing off the logo or anywhere. no arrows. our logo altered in anyway. no broken circles. no variences in blue. we like our logo the way it is. the font is monotype corsiva

```html
<!DOCTYPE html>
<html lang="en">
<head>
<meta charset="utf-8">
<title>Trquillaris Advisory Letterhead</title>
<link href="https://fonts.googleapis.com/css2?family=Carlito:wght@400;700&display=swap" rel="stylesheet">
<style>
  :root {
    --brand-blue: #3590c8;
    --brand-grey: #636466;
    --ink: #1d1d1d;
    --paper: #ffffff;
    --backdrop: #ececec;
    --photo-tone: #b9b9b9;
    --signature-tone: #e6e6e6;
  }
  * { margin: 0; padding: 0; box-sizing: border-box; }
  html, body {
    width: 1200px; height: 1200px; overflow: hidden;
    background: var(--backdrop);
    font-family: "Carlito", "Calibri", sans-serif;
    color: var(--ink);
  }
  .letterhead {
    position: absolute; left: 160px; top: 30px;
    width: 880px; height: 1139px;
    background: var(--paper);
    overflow: hidden;
  }
  .brand-mark {
    position: absolute; left: 89px; top: 61px;
    width: 104px; height: 104px;
    border: 4px solid var(--brand-blue); border-radius: 50%;
  }
  .brand-name {
    position: absolute; left: 210px; top: 95px;
    font-size: 29px; font-weight: 400; color: var(--brand-blue);
    white-space: nowrap;
  }
  .contact-rule {
    position: absolute; left: 580px; top: 70px;
    width: 1.5px; height: 64px; background: var(--brand-blue);
  }
  .contact-list {
    position: absolute; left: 588px; top: 69px;
    list-style: none; font-size: 12.5px; line-height: 15px;
  }
  .contact-list li { display: flex; align-items: center; gap: 5px; }
  .contact-list li.gap { margin-top: 6px; }
  .contact-list svg { width: 12px; height: 12px; flex: none; }
  .letter-body {
    position: absolute; left: 82px; top: 241px; width: 690px;
    font-size: 15.6px; line-height: 30px;
  }
  .letter-body h1 { font-size: 15.6px; font-weight: 700; margin-bottom: 30px; }
  .letter-body p { margin-bottom: 30px; }
  .sign-off { position: absolute; left: 82px; top: 845px; font-size: 15.6px; }
  .signature {
    position: absolute; left: 82px; top: 868px;
    width: 214px; height: 74px; background: var(--signature-tone); border-radius: 4px;
  }
  .signer-title { position: absolute; left: 82px; top: 965px; font-size: 15.6px; }
  .footer-wave { position: absolute; left: 0; bottom: 0; width: 880px; height: 122px; }
  .portrait {
    position: absolute; left: 674px; top: 996px;
    width: 124px; height: 124px; border-radius: 50%;
    border: 5px solid var(--brand-blue);
    background: radial-gradient(circle at 50% 40%, #d6d6d6, var(--photo-tone) 60%, #4a4a4a);
  }
</style>
</head>
<body>
<main class="letterhead">
  <header>
    <div class="brand-mark"></div>
    <div class="brand-name">Trquillaris Advisory, LLC</div>
    <div class="contact-rule"></div>
    <ul class="contact-list">
      <li><svg viewBox="0 0 12 12"><circle cx="6" cy="6" r="6" fill="var(--brand-blue)"/><path d="M3 4.5h6v3.5H3z" fill="#fff"/></svg>5829017763</li>
      <li><svg viewBox="0 0 12 12"><circle cx="6" cy="6" r="6" fill="var(--brand-blue)"/><path d="M3 4.5h6v3.5H3z" fill="#fff"/></svg>6148250397</li>
      <li class="gap"><svg viewBox="0 0 12 12"><circle cx="6" cy="6" r="6" fill="var(--brand-blue)"/><path d="M3 4h6v4.5H3z M3 4l3 2.5L9 4" fill="#fff" stroke="var(--brand-blue)" stroke-width=".6"/></svg>info@trquillarisadvisory.solutions</li>
      <li><svg viewBox="0 0 12 12"><circle cx="6" cy="6" r="6" fill="var(--brand-blue)"/><circle cx="6" cy="6" r="3.2" fill="none" stroke="#fff" stroke-width=".9"/><path d="M2.8 6h6.4M6 2.8v6.4" stroke="#fff" stroke-width=".7"/></svg>www.trquillarisadvisory.solutions</li>
    </ul>
  </header>

  <section class="letter-body">
    <h1>Lorem Ipsum is simply</h1>
    <p>&nbsp;dummy text of the printing and typesetting industry. Lorem Ipsum has been the industry's standard dummy text ever since the 1500s, when an unknown printer took a galley of type and scrambled it to make a type specimen book. It has survived not only five centuries, but also the leap into electronic typesetting, remaining essentially unchanged.</p>
    <p>It is a long established fact that a reader will be distracted by the readable content of a page when looking at its layout. The point of using Lorem Ipsum is that it has a more-or-less normal distribution of letters, as opposed to using 'Content here, content here', making it look like readable English. Many desktop publishing packages and web page editors now use Lorem Ipsum as their default model text, and a search for 'lorem ipsum' will uncover many web sites still in their infancy. Various versions have evolved over the years, sometimes by accident, sometimes on purpose (injected humour and the like).</p>
    <p>&nbsp;Contrary to popular belief, Lorem Ipsum is not simply random text. It has roots in a piece of classical Latin literature from 45 BC, making it over 2000 years old. Aldric Venmoor, a Latin professor at Corwell-Ashby College in Virginia, looked up one of the more obscure Latin words, consectetur, from a Lorem Ipsum passage,</p>
  </section>

  <div class="sign-off">Lorem Ipsum</div>
  <div class="signature" role="img" aria-label="Handwritten signature"></div>
  <div class="signer-title">Lorem Ipsum is a dummy</div>

  <svg class="footer-wave" viewBox="0 880 761 105" preserveAspectRatio="none" aria-hidden="true">
    <path d="M170,905 C300,898 420,905 560,925 C640,935 700,910 761,893 L761,930 C680,945 620,948 560,940 C420,922 300,906 170,905Z" fill="var(--brand-blue)"/>
    <path d="M0,935 C120,905 260,900 400,918 C520,934 640,955 761,950 L761,985 L0,985Z" fill="var(--brand-grey)"/>
    <path d="M0,965 C100,932 230,915 330,925 C400,935 460,960 500,985 L0,985Z" fill="var(--brand-blue)"/>
  </svg>
  <div class="portrait" role="img" aria-label="Portrait photograph of the consultant"></div>
</main>
</body>
</html>
```